Business card design needed

I am a musculoskeletal therapist and pride myself in offering a top service. The market is very competitive and therefore the card needs to reflect professionalism and trust.

Industry/Entity Type

Business

Contact Information for Business Card

Business: Balanced Kinetics
Message: Muscle, Nerve & Joint Pain Management
Name: Laurent Dubreuil
Title: Remedial Therapist
Phone: 0471 968 203
Display: Nice anatomical image of a body targeting/circling the muscle, spine and nerve in 3 circles. Next to the image a logo with the letters BK.

```html
<!DOCTYPE html>
<html lang="en">
<head>
<meta charset="utf-8">
<title>Balanced Kinetics – Business Card</title>
<link href="https://fonts.googleapis.com/css2?family=Open+Sans:wght@400;600;700&display=swap" rel="stylesheet">
<style>
  :root {
    --page-bg: #e6e9ec;
    --card-white: #ffffff;
    --brand-blue: #1b7fcc;
    --brand-blue-deep: #1571bd;
    --wave-light: #16a9ea;
    --text-grey: #4a4f55;
    --accent-orange: #f5a623;
    --circle-pale: #dcebf7;
  }
  * { box-sizing: border-box; margin: 0; padding: 0; }
  html, body { width: 1200px; height: 1000px; overflow: hidden; }
  body {
    background: var(--page-bg);
    font-family: "Open Sans", Arial, sans-serif;
    display: flex;
    flex-direction: column;
    align-items: center;
    justify-content: center;
    gap: 70px;
  }
  .card {
    position: relative;
    width: 600px;
    height: 345px;
    background: var(--card-white);
    box-shadow: 0 12px 30px rgba(30, 50, 70, 0.18);
    overflow: hidden;
  }
  .card-wave { position: absolute; inset: 0; width: 100%; height: 100%; }

  .brand {
    position: absolute;
    display: flex;
    flex-direction: column;
    align-items: flex-start;
  }
  .brand-row { display: flex; align-items: center; gap: 8px; }
  .brand-dot { width: 20px; height: 20px; border-radius: 50%; }
  .brand-name { font-weight: 400; letter-spacing: 0.2px; }
  .brand-tagline {
    font-size: 10.5px;
    letter-spacing: 1px;
    margin-top: 2px;
  }

  .card-front .brand { top: 40px; right: 44px; }
  .card-front .brand-dot { background: var(--brand-blue); }
  .card-front .brand-name { font-size: 27px; color: var(--brand-blue); }
  .card-front .brand-tagline {
    color: var(--text-grey);
    border-top: 2px solid var(--brand-blue);
    padding-top: 2px;
    margin-left: 28px;
  }

  .holder { position: absolute; left: 40px; top: 205px; color: #fff; }
  .holder-name { font-size: 25px; font-weight: 700; }
  .holder-title { font-size: 13px; font-weight: 400; margin-top: 0; }
  .holder-phone {
    display: flex; align-items: center; gap: 6px;
    margin-top: 32px; font-size: 15px;
  }
  .holder-phone svg { width: 13px; height: 13px; }

  .card-back .mark-circle {
    position: absolute;
    left: 100px; top: 30px;
    width: 130px; height: 130px;
    border-radius: 50%;
    background: var(--circle-pale);
  }
  .card-back .brand { right: 40px; bottom: 56px; }
  .card-back .brand-dot { background: #fff; }
  .card-back .brand-name { font-size: 22px; color: #fff; }
  .card-back .brand-tagline { color: #eaf4fc; font-size: 9px; margin-left: 28px; }
</style>
</head>
<body>

  <section class="card card-front" aria-label="Card front">
    <svg class="card-wave" viewBox="0 0 600 345" preserveAspectRatio="none" aria-hidden="true">
      <path d="M0,40 C60,150 170,200 280,200 C360,200 400,165 460,185 C540,215 585,300 600,345 L0,345 Z" fill="var(--wave-light)"/>
      <path d="M0,75 C70,175 175,222 285,220 C365,218 405,190 465,208 C535,232 575,305 590,345 L0,345 Z" fill="var(--brand-blue)"/>
    </svg>
    <div class="brand">
      <div class="brand-row">
        <span class="brand-dot"></span>
        <span class="brand-name">Balanced Kinetics</span>
      </div>
      <span class="brand-tagline">Muscle - Nerve - Joint Pain Management</span>
    </div>
    <div class="holder">
      <div class="holder-name">Laurent Dubreuil</div>
      <div class="holder-title">Remedial Therapist</div>
      <div class="holder-phone">
        <svg viewBox="0 0 24 24" aria-hidden="true"><path fill="var(--accent-orange)" d="M6.6 10.8a15.1 15.1 0 0 0 6.6 6.6l2.2-2.2a1 1 0 0 1 1-.25 11.4 11.4 0 0 0 3.6.57 1 1 0 0 1 1 1V20a1 1 0 0 1-1 1A17 17 0 0 1 3 4a1 1 0 0 1 1-1h3.5a1 1 0 0 1 1 1c0 1.25.2 2.45.57 3.6a1 1 0 0 1-.25 1z"/></svg>
        <span>0471 968 203</span>
      </div>
    </div>
  </section>

  <section class="card card-back" aria-label="Card back">
    <svg class="card-wave" viewBox="0 0 600 345" preserveAspectRatio="none" aria-hidden="true">
      <path d="M0,345 C90,300 170,200 300,170 C420,140 520,140 600,60 L600,345 Z" fill="var(--wave-light)"/>
      <path d="M0,345 C100,315 190,225 310,198 C430,172 530,170 600,95 L600,345 Z" fill="var(--brand-blue-deep)"/>
    </svg>
    <span class="mark-circle" aria-hidden="true"></span>
    <div class="brand">
      <div class="brand-row">
        <span class="brand-dot"></span>
        <span class="brand-name">Balanced Kinetics</span>
      </div>
      <span class="brand-tagline">Muscle - Nerve - Joint Pain Management</span>
    </div>
  </section>

</body>
</html>
```